Creating the Look and Feel of an Elite Boutique Consulting Practice: Kestrel Advisory

Complete a professional website on Weebly. As part of the site, we are open to a new logo -- we have just launched. We put up a starter website that shows you the content and theme we are going for. But clearly we aren't professional web designers and we need your help. Check out our start at kestreladvisory.com

Target Market(s)

Fortune 500 Clients

Industry/Entity Type

Management Consulting

Logo Text

KESTREL Advisory

Number of Pages Required

4 page

Requirements
Must have
• I've already set us up on Weebly. I'd like to give the selected designer the log-in credentials and have the designer create it on Weebly, so we can maintain it through that service.

```html
<!DOCTYPE html>
<html lang="en">
<head>
<meta charset="utf-8">
<title>Kestrel Advisory</title>
<link rel="stylesheet" href="https://fonts.googleapis.com/css2?family=Hind:wght@400;500;600;700&display=swap">
<style>
  :root {
    --ink: #111111;
    --paper: #ffffff;
    --nav-bar: rgba(22, 30, 40, 0.78);
    --nav-link: #8fb4e6;
    --nav-active: #ffffff;
    --sky-top: #5d7384;
    --sky-mid: #c9b79a;
    --city-dark: #1c2530;
    --button-fill: #d4d4d4;
    --button-ink: #1e1e1e;
    --rule: #c8c8c8;
    --footer: #3a3a3a;
    --footer-ink: #d6d6d6;
    --photo-light: #eef0f3;
    --photo-blue: #3f86c9;
    --photo-dark: #1a1d22;
  }
  * { box-sizing: border-box; margin: 0; padding: 0; }
  html, body { width: 784px; height: 1200px; overflow: hidden; background: var(--paper); }
  body { font-family: "Hind", sans-serif; color: var(--ink); position: relative; }

  .hero {
    position: absolute; left: 0; top: 0; width: 784px; height: 494px;
    background:
      linear-gradient(180deg, var(--sky-top) 0%, #8c96a0 22%, var(--sky-mid) 40%, #6c7178 52%, #2b3541 66%, var(--city-dark) 100%);
  }
  .site-header {
    position: absolute; left: 0; top: 0; width: 784px; height: 58px;
    background: var(--nav-bar);
  }
  .brand {
    position: absolute; left: 34px; top: 16px;
    font-size: 20px; font-weight: 400; color: var(--paper); letter-spacing: 0.2px;
  }
  .main-nav { position: absolute; top: 26px; right: 42px; display: flex; gap: 24px; }
  .main-nav a {
    font-size: 10px; font-weight: 500; color: var(--nav-link);
    text-decoration: none; letter-spacing: -0.2px;
  }
  .main-nav a.is-current { color: var(--nav-active); }

  .hero-copy { position: absolute; left: 0; top: 252px; width: 784px; text-align: center; color: var(--paper); }
  .hero-title { font-size: 19px; font-weight: 400; letter-spacing: 0.3px; }
  .hero-sub { font-size: 12px; margin-top: 6px; letter-spacing: 0.4px; }
  .hero-button {
    position: absolute; left: 322px; top: 355px; width: 139px; height: 32px;
    background: var(--button-fill); color: var(--button-ink);
    font-size: 10px; font-weight: 500; letter-spacing: 0.4px;
    display: flex; align-items: center; justify-content: center;
  }

  .section-title { position: absolute; font-size: 15px; font-weight: 700; }
  .services-title { left: 61px; top: 533px; }
  .people-title { left: 51px; top: 900px; }

  .photo {
    position: absolute;
    background: radial-gradient(circle at 70% 45%, var(--photo-blue) 0%, #6aa6d8 18%, transparent 34%),
                linear-gradient(90deg, var(--photo-light) 0%, #e3e6ea 60%, var(--photo-dark) 100%);
  }
  .card-photo { top: 571px; width: 192px; height: 155px; }
  .person-photo { top: 940px; width: 159px; height: 155px; }

  .blurb { position: absolute; font-size: 12.2px; line-height: 14.6px; font-weight: 500; }
  .blurb p + p { margin-top: 8.5px; }
  .card-blurb { top: 738px; width: 200px; }
  .person-blurb { top: 955px; width: 175px; }

  .divider { position: absolute; left: 58px; top: 867px; width: 668px; height: 1px; background: var(--rule); }

  .site-footer {
    position: absolute; left: 0; top: 1132px; width: 784px; height: 68px; background: var(--footer);
  }
  .copyright { position: absolute; left: 45px; top: 30px; font-size: 9px; color: var(--footer-ink); }
  .social { position: absolute; right: 44px; top: 30px; display: flex; gap: 11px; }
  .social span { width: 10px; height: 10px; border-radius: 50%; background: var(--footer-ink); }
</style>
</head>
<body>
  <section class="hero" role="img" aria-label="Skyline photograph of a city at dusk with tall towers"></section>

  <header class="site-header">
    <div class="brand">Kestrel Advisory</div>
    <nav class="main-nav">
      <a class="is-current" href="#">ABOUT KESTREL</a>
      <a href="#">APPROACH</a>
      <a href="#">TEAM</a>
      <a href="#">CONTACT</a>
    </nav>
  </header>

  <div class="hero-copy">
    <h1 class="hero-title">DO YOU NEED TO TRANSFORM YOUR ORGANIZATION?</h1>
    <p class="hero-sub">Let's plot your path to success.</p>
  </div>
  <div class="hero-button">LEARN MORE</div>

  <h2 class="section-title services-title">We help your organization achieve a successful.</h2>

  <div class="photo card-photo" style="left:49px" role="img" aria-label="Hand holding a glowing globe surrounded by floating screens"></div>
  <div class="photo card-photo" style="left:296px" role="img" aria-label="Hand holding a glowing globe surrounded by floating screens"></div>
  <div class="photo card-photo" style="left:543px" role="img" aria-label="Hand holding a glowing globe surrounded by floating screens"></div>

  <div class="blurb card-blurb" style="left:51px">
    <p>Partnering with you to clarify<br>and communicate your<br>transformational purpose.</p>
    <p>Where are you going?<br>What will you become?<br>Why change now?</p>
  </div>
  <div class="blurb card-blurb" style="left:298px">
    <p>Partnering with you to clarify<br>and communicate your<br>transformational purpose.</p>
    <p>Where are you going?<br>What will you become?<br>Why change now?</p>
  </div>
  <div class="blurb card-blurb" style="left:545px">
    <p>Partnering with you to clarify<br>and communicate your<br>transformational purpose.</p>
    <p>Where are you going?<br>What will you become?<br>Why change now?</p>
  </div>

  <div class="divider"></div>

  <h2 class="section-title people-title">The people of KESTREL Advisory&nbsp; are:</h2>

  <div class="photo person-photo" style="left:40px" role="img" aria-label="Hand holding a glowing globe surrounded by floating screens"></div>
  <div class="blurb person-blurb" style="left:218px">
    <p>Partnering with you to clarify<br>and communicate your<br>transformational purpose.</p>
    <p>Where are you going?<br>What will you become?<br>Why change now?</p>
  </div>
  <div class="photo person-photo" style="left:403px" role="img" aria-label="Hand holding a glowing globe surrounded by floating screens"></div>
  <div class="blurb person-blurb" style="left:581px">
    <p>Partnering with you to clarify<br>and communicate your<br>transformational purpose.</p>
    <p>Where are you going?<br>What will you become?<br>Why change now?</p>
  </div>

  <footer class="site-footer">
    <p class="copyright">© 2015 KESTREL ADVISORY</p>
    <div class="social" aria-label="Social links"><span></span><span></span><span></span></div>
  </footer>
</body>
</html>
```